Swim School Certificates

We are looking to have some certificates designed for our Learn to Swim School. These will be handed out to our students when they complete each level. We will need different certificates for each level, however, we would like a consistent theme throughout, so each level may only have a slight variation. We are happy for you to just show us a couple of variations to begin with, so we can see how these would work. Then once we decide on the winning design, you can complete the rest.
The levels are:
Bubs 1
Bubs 2
Toddler 1
Toddler 2
Beginner 1
Beginner 2
Beginner 3
Stroke Development 1
Stroke Development 2
Advanced 1
Advanced 2
Squad
The Certificates should include:
Congratulations to:
(blank line for name)
You have completed (level name), Keep up the good work!!!
Signed: (blank line) Date: (blank line)
I've included a copy of our logo, and a copy of our governing bodies logo both of which should be included on the certificate.
I've also included some examples of certificates we like, to give you an idea of our style. We are happy for the bubs and toddler certificates to be more child focused, so they can included a kid friendly element to them, however this will need to reduce to a more simplistic design as the levels increase into beginner and stroke etc.
You can also look on our Facebook page to get an idea of what we do.
https://www.facebook.com/coralreefswimschool/?ref=bookmarks
We will also need editable source files upon completion as we may be looking to change the name of some classes in the future.
Please let us know if you need any of the files in other formats
Kind Regards
Maree

```html
<!DOCTYPE html>
<html lang="en">
<head>
<meta charset="utf-8">
<title>Learn to Swim Certificate – Bubs 1</title>
<link href="https://fonts.googleapis.com/css2?family=Leckerli+One&family=Montserrat:wght@600;700&family=Questrial&display=swap" rel="stylesheet">
<style>
  :root {
    --page-bg: #e8e5e0;
    --paper: #ffffff;
    --blue-deep: #1d59a3;
    --blue-mid: #3a8fd0;
    --blue-light: #7cc6ec;
    --frame-line: rgba(255,255,255,0.75);
    --title-green: #3fc94f;
    --title-teal: #16a3b8;
    --title-blue: #1561b0;
    --label-navy: #2a4b9b;
    --placeholder: #9a9a9a;
    --star-green: #49b848;
    --star-yellow: #f5d21c;
    --star-navy: #2c3f95;
    --star-red: #e3262d;
    --logo-blue: #58b4e6;
  }
  * { box-sizing: border-box; margin: 0; padding: 0; }
  html, body { width: 1200px; height: 1200px; overflow: hidden; }
  body { background: var(--page-bg); position: relative; }

  .certificate {
    position: absolute; left: 40px; top: 204px;
    width: 1120px; height: 792px;
    background: var(--paper);
    padding: 11px;
    box-shadow: 0 2px 8px rgba(0,0,0,0.15);
  }
  .certificate__panel {
    position: relative; width: 100%; height: 100%;
    background: linear-gradient(180deg, var(--blue-deep) 0%, var(--blue-mid) 45%, var(--blue-light) 100%);
    overflow: hidden;
  }
  .certificate__frame {
    position: absolute; inset: 12px;
    border: 2px solid var(--frame-line);
    pointer-events: none; z-index: 5;
  }
  .centered { position: absolute; left: 0; right: 0; text-align: center; }

  .title {
    top: 40px;
    font-family: "Leckerli One", cursive;
    font-size: 112px; line-height: 1.1;
    background: linear-gradient(180deg, var(--title-green) 10%, var(--title-teal) 60%, var(--title-blue) 100%);
    -webkit-background-clip: text; background-clip: text;
    color: transparent;
  }
  .congrats {
    top: 193px;
    font-family: "Montserrat", sans-serif; font-weight: 600;
    font-size: 42px; color: #fff;
  }
  .name-field {
    position: absolute; left: 258px; top: 258px;
    width: 581px; height: 44px;
    background: #fff; border-radius: 9px;
    box-shadow: inset 0 -2px 4px rgba(0,0,0,0.15);
    font-family: "Questrial", sans-serif; font-size: 27px;
    letter-spacing: 7px; color: var(--placeholder);
    text-align: center; line-height: 44px;
  }
  .completed {
    top: 315px;
    font-family: "Questrial", sans-serif; font-size: 48px; color: #fff;
  }
  .level-row {
    position: absolute; left: 0; right: 0; top: 384px;
    display: flex; justify-content: center; align-items: center; gap: 14px;
  }
  .level-row svg { display: block; }
  .level-name {
    margin: 0 14px;
    font-family: "Montserrat", sans-serif; font-weight: 700;
    font-size: 44px; letter-spacing: -2px;
    background: linear-gradient(180deg, var(--title-green), var(--title-blue));
    -webkit-background-clip: text; background-clip: text; color: transparent;
  }
  .encourage {
    top: 432px;
    font-family: "Questrial", sans-serif; font-size: 48px; color: #fff;
  }
  .sign-line {
    position: absolute; height: 1px; background: rgba(40,80,150,0.45); top: 555px;
  }
  .sign-line--signed { left: 70px; width: 300px; }
  .sign-line--date { left: 803px; width: 275px; }
  .label {
    position: absolute;
    font-family: "Montserrat", sans-serif; font-weight: 700;
    font-size: 25px; color: var(--label-navy);
  }
  .label--signed { left: 146px; top: 562px; }
  .label--date { left: 859px; top: 553px; }

  .swimmer-photo {
    position: absolute; left: 302px; top: 518px;
    width: 500px; height: 252px;
    background: radial-gradient(ellipse at 55% 60%, #c7e7f4 0%, #8fcbe8 45%, rgba(124,198,236,0) 75%);
  }
  .water-wave {
    position: absolute; left: 0; bottom: 0; width: 100%; height: 150px;
  }
  .badge {
    position: absolute; left: 137px; top: 608px;
    width: 128px; height: 128px; border-radius: 50%;
    background: #fff; border: 8px solid #2e86cc;
  }
  .school-mark {
    position: absolute; left: 838px; top: 602px;
    width: 128px; height: 128px; border-radius: 50%;
    background: #fff; border: 3px solid var(--logo-blue);
    display: flex; align-items: center; justify-content: center; text-align: center;
    font-family: "Questrial", sans-serif; font-size: 19px; line-height: 1.15;
    color: var(--logo-blue); padding: 10px;
  }
</style>
</head>
<body>
  <main class="certificate">
    <div class="certificate__panel">
      <svg class="water-wave" viewBox="0 0 1098 150" preserveAspectRatio="none" aria-hidden="true">
        <path d="M0 90 C 200 40, 350 120, 560 80 S 900 40, 1098 60 L1098 150 L0 150 Z" fill="#a8dcf2" opacity="0.55"/>
        <path d="M0 115 C 250 80, 450 140, 700 105 S 960 90, 1098 100 L1098 150 L0 150 Z" fill="#d2eef9" opacity="0.6"/>
      </svg>

      <h1 class="centered title">Learn to Swim</h1>
      <p class="centered congrats">Congratulations to</p>
      <div class="name-field">Learner’s Name</div>
      <p class="centered completed">You have completed</p>

      <div class="level-row">
        <svg width="44" height="44" viewBox="0 0 24 24"><polygon fill="var(--star-green)" points="12,1 15,9 23,9 16.5,14 19,22 12,17 5,22 7.5,14 1,9 9,9"/></svg>
        <svg width="40" height="40" viewBox="0 0 24 24"><polygon fill="var(--star-yellow)" points="12,1 15,9 23,9 16.5,14 19,22 12,17 5,22 7.5,14 1,9 9,9"/></svg>
        <svg width="36" height="36" viewBox="0 0 24 24"><polygon fill="var(--star-navy)" points="12,1 15,9 23,9 16.5,14 19,22 12,17 5,22 7.5,14 1,9 9,9"/></svg>
        <svg width="30" height="30" viewBox="0 0 24 24"><polygon fill="var(--star-red)" points="12,1 15,9 23,9 16.5,14 19,22 12,17 5,22 7.5,14 1,9 9,9"/></svg>
        <span class="level-name">BUBS 1</span>
        <svg width="30" height="30" viewBox="0 0 24 24"><polygon fill="var(--star-red)" points="12,1 15,9 23,9 16.5,14 19,22 12,17 5,22 7.5,14 1,9 9,9"/></svg>
        <svg width="36" height="36" viewBox="0 0 24 24"><polygon fill="var(--star-navy)" points="12,1 15,9 23,9 16.5,14 19,22 12,17 5,22 7.5,14 1,9 9,9"/></svg>
        <svg width="40" height="40" viewBox="0 0 24 24"><polygon fill="var(--star-yellow)" points="12,1 15,9 23,9 16.5,14 19,22 12,17 5,22 7.5,14 1,9 9,9"/></svg>
        <svg width="44" height="44" viewBox="0 0 24 24"><polygon fill="var(--star-green)" points="12,1 15,9 23,9 16.5,14 19,22 12,17 5,22 7.5,14 1,9 9,9"/></svg>
      </div>

      <p class="centered encourage">Keep up the good work!!!</p>

      <div class="sign-line sign-line--signed"></div>
      <div class="sign-line sign-line--date"></div>
      <span class="label label--signed">SIGNED:</span>
      <span class="label label--date">DATE:</span>

      <div class="swimmer-photo" role="img" aria-label="Photo of a young swimmer doing freestyle in splashing pool water"></div>

      <div class="badge" role="img" aria-label="Governing body registration badge"></div>
      <div class="school-mark">Coral Reef Swim School</div>

      <div class="certificate__frame"></div>
    </div>
  </main>
</body>
</html>
```